Capability statement. I’ll send through what I put into GPT. Once layout is sorted I can send through more images

Target Market(s)

Tier 1 and 2 contractors

Industry/Entity Type

Civil construction

Colors
00AB8E
00BBA5
67D7C9
C6EFE9
E9F9F6

Requirements
Must have
• Black backgrounds and Matt charcoal/aqua colour scheme

```html
<!DOCTYPE html>
<html lang="en">
<head>
<meta charset="utf-8">
<title>Ardent Civil Group – Capability Statement</title>
<link href="https://fonts.googleapis.com/css2?family=Bebas+Neue&family=Poppins:wght@400;500;600&display=swap" rel="stylesheet">
<style>
:root{
  --stage:#e4e3e4;
  --ink:#0b0c0d;
  --charcoal:#16191b;
  --aqua:#00bba5;
  --aqua-deep:#00ab8e;
  --aqua-soft:#67d7c9;
  --mint:#c6eFE9;
  --mist:#e9f9f6;
  --white:#ffffff;
  --grey:#c9cdcf;
  --muted:#8a9194;
  --line:#1f5d57;
}
*{box-sizing:border-box;margin:0;padding:0}
html,body{width:1200px;height:1038px;overflow:hidden;background:var(--stage)}
body{position:relative;font-family:'Poppins',sans-serif;color:var(--white)}
.page{position:absolute;width:342px;height:443px;background:var(--ink);overflow:hidden}
.p1{left:51px;top:57px}.p2{left:427px;top:57px}.p3{left:803px;top:57px}
.p4{left:51px;top:536px}.p5{left:427px;top:536px}
.abs{position:absolute}
.photo{position:absolute}
.brand{position:absolute;left:22px;top:22px;font-family:'Bebas Neue',sans-serif;color:#d9dcdd;line-height:.9}
.brand .name{font-size:36px;letter-spacing:1px;display:block}
.brand .sub{font-size:12.5px;letter-spacing:5.2px;display:block}
.tags{position:absolute;left:22px;top:86px;font-family:'Bebas Neue',sans-serif;font-size:6.6px;letter-spacing:.3px;color:var(--grey)}
.tags span{margin:0 3px;color:var(--aqua)}
.title{position:absolute;left:22px;font-family:'Bebas Neue',sans-serif;line-height:.92;color:var(--white)}
.title .teal{color:var(--aqua)}
.rule{position:absolute;left:22px;width:15px;height:1px;background:var(--grey)}
.lede{position:absolute;left:22px;font-size:6.2px;line-height:1.55;color:var(--grey)}
.lede em{font-style:normal;color:var(--aqua)}
.h{position:absolute;font-size:10px;font-weight:600;padding-left:5px;border-left:2px solid var(--aqua);line-height:1}
.list{position:absolute;list-style:none;font-size:5.8px;color:var(--grey)}
.list li{position:relative;padding-left:7px}
.list li::before{content:"";position:absolute;left:0;top:2.2px;width:3.2px;height:3.2px;border:.7px solid var(--aqua);border-radius:50%}
.foot{position:absolute;left:22px;right:22px;top:421px;display:flex;align-items:center;gap:4px;font-family:'Bebas Neue',sans-serif;font-size:5.6px;color:var(--grey)}
.foot .no{color:var(--aqua)}
.foot .bar{flex:1;height:.6px;background:var(--line);margin-left:6px}
.divider{position:absolute;left:0;right:0;height:1px;background:var(--line)}
.card{position:absolute;border:.6px solid var(--line);background:var(--charcoal)}
.card .cap{position:absolute;left:4px;right:4px;font-size:4.6px;line-height:1.35;color:var(--grey)}
.card .cap b{display:block;color:var(--aqua);font-weight:500}
.tile-label{position:absolute;left:0;right:0;bottom:0;height:11px;background:rgba(8,10,11,.85);font-size:4.5px;font-weight:500;color:var(--white);display:flex;align-items:center;padding-left:15px}
.tile-label::before{content:"";position:absolute;left:5px;top:3px;width:5px;height:5px;border:.7px solid var(--aqua);border-radius:50%}
.stat{position:absolute;border:.6px solid #2b3336;height:20px;display:flex;align-items:center;gap:4px;padding:0 4px;font-size:4.8px;color:var(--grey);line-height:1.15}
.stat b{display:block;font-size:7.5px;font-weight:500;color:var(--white)}
.stat i{width:13px;height:13px;border:.7px solid var(--aqua);border-radius:3px;flex:none}
.rowline{position:absolute;display:flex;gap:6px;font-size:5.8px;color:var(--grey)}
/* cover */
.badge{position:absolute;left:29px;top:0;width:79px;height:85px;background:#0f6c72;clip-path:polygon(0 0,100% 0,100% 84%,50% 100%,0 84%)}
.badge .name{position:absolute;left:8px;top:20px;font-family:'Bebas Neue',sans-serif;font-size:21px;color:var(--white);line-height:.9}
.badge .name small{display:block;font-size:8px;letter-spacing:3px}
.badge .t{position:absolute;left:8px;top:62px;font-size:3px;color:var(--mint);letter-spacing:.2px}
.cover-feats{position:absolute;left:21px;right:21px;top:392px;display:flex;font-size:5.6px;line-height:1.25;color:var(--white)}
.cover-feats div{flex:1;display:flex;align-items:center;gap:5px;padding-left:3px;border-left:.6px solid rgba(255,255,255,.3)}
.cover-feats div:first-child{border:0;padding-left:0}
.cover-feats i{width:12px;height:12px;border:.8px solid var(--aqua-soft);border-radius:50%}
.cover-svcs{position:absolute;left:21px;right:21px;top:421px;display:flex;justify-content:space-between;font-size:5.8px;color:var(--white)}
.cover-svcs span.d{color:var(--aqua)}
.mini-stats{position:absolute;left:21px;right:21px;top:383px;display:flex;justify-content:space-between;font-size:3.6px;color:var(--grey);line-height:1.3}
.mini-stats div{display:flex;gap:3px;align-items:center}
.mini-stats b{display:block;color:var(--aqua);font-weight:500;font-size:4.4px}
.mini-stats i{width:10px;height:10px;border:.7px solid var(--aqua);border-radius:50%;flex:none}
/* brand mark */
.mark{position:absolute;left:832px;top:640px;width:290px;font-family:'Bebas Neue',sans-serif;color:var(--white)}
.mark .name{font-size:86px;line-height:.85;letter-spacing:3px;display:block}
.mark .sub{font-size:30px;letter-spacing:15.5px;display:block;line-height:1}
.mark .ln{height:1.2px;background:var(--aqua);margin:28px 0 8px}
.mark .tg{font-size:17px;color:var(--aqua-soft);display:flex;justify-content:space-between;letter-spacing:.3px}
</style>
</head>
<body>

<!-- Cover -->
<section class="page p1">
  <div class="photo" role="img" aria-label="Teal excavator loading an articulated dump truck on a dirt site under blue sky" style="inset:0;background:linear-gradient(180deg,#2f7fe0 0%,#5aa0ee 28%,#6f7f70 45%,#6b5437 62%,#2a2118 82%,#121010 100%)"></div>
  <div class="badge"><span class="name">ARDENT<small>CIVIL GROUP</small></span><span class="t">EARTHWORKS | INFRASTRUCTURE | PLANT HIRE</span></div>
  <div class="title" style="top:280px;font-size:33px">CAPABILITY<br><span class="teal">STATEMENT</span></div>
  <div class="rule" style="top:344px;left:21px;background:var(--aqua)"></div>
  <div class="lede" style="left:21px;top:352px;color:var(--white)">Delivering Civil Infrastructure,<br>Earthworks &amp; Drainage Solutions<br><em>Across NSW</em></div>
  <div class="cover-feats">
    <div><i></i>EXPERIENCED<br>TEAM</div><div><i></i>MODERN<br>FLEET</div><div><i></i>SAFETY<br>FOCUSED</div><div><i></i>PROVEN<br>DELIVERY</div>
  </div>
  <div class="cover-svcs"><span>BULK EARTHWORKS</span><span class="d">•</span><span>DETAILED EXCAVATION</span><span class="d">•</span><span>DRAINAGE</span><span class="d">•</span><span>ROADWORKS</span><span class="d">•</span><span>PLANT HIRE</span></div>
</section>

<!-- About -->
<section class="page p2">
  <div class="photo" role="img" aria-label="Aerial view of an excavator digging a long trench beside trees" style="left:150px;top:0;width:192px;height:228px;background:linear-gradient(160deg,#2f4a26,#566b3a 40%,#8a7a5c 65%,#4d6b35)"></div>
  <div class="brand"><span class="name">ARDENT</span><span class="sub">CIVIL GROUP</span></div>
  <div class="tags">EARTHWORKS<span>|</span>INFRASTRUCTURE<span>|</span>PLANT HIRE</div>
  <div class="title" style="top:101px;font-size:27px">ABOUT<br><span class="teal" style="font-size:21px">ARDENT CIVIL GROUP</span></div>
  <div class="rule" style="top:153px"></div>
  <div class="lede" style="top:159px">Sydney-based civil construction<br>and plant hire contractor delivering<br>earthworks, drainage, utilities and<br>infrastructure projects across NSW.</div>
  <div class="h" style="left:22px;top:210px">Company Snapshot</div>
  <div class="stat" style="left:22px;top:228px;width:61px"><i></i><span><b>20 +</b>Plant Asset</span></div>
  <div class="stat" style="left:85px;top:228px;width:76px"><i></i><span><b>15+</b>Skilled Personnel</span></div>
  <div class="stat" style="left:22px;top:253px;width:78px"><i></i><span><b>1.7T-50T</b>Excavator fleet</span></div>
  <div class="stat" style="left:105px;top:253px;width:94px"><i></i><span><b>ISO</b>accredited systems</span></div>
  <div class="stat" style="left:207px;top:253px;width:106px"><i></i><span><b>NSW</b>Statewide Capability</span></div>
  <div class="h" style="left:22px;top:289px">Core Services</div>
  <ul class="list" style="left:22px;top:304px;line-height:12.6px;columns:1"><li>Bulk Earthworks</li><li>Utilities &amp; Services</li></ul>
  <ul class="list" style="left:92px;top:304px;line-height:12.6px"><li>Detailed Excavation</li><li>Civil Infrastructure</li></ul>
  <ul class="list" style="left:176px;top:304px;line-height:12.6px"><li>Stormwater Drainage</li></ul>
  <ul class="list" style="left:261px;top:304px;line-height:12.6px"><li>Road Construction</li></ul>
  <div class="h" style="left:22px;top:338px">Fleet Capability</div>
  <ul class="list" style="left:22px;top:353px;line-height:12.4px"><li>Excavators 1.7T-50T (GPS Equipped)</li><li>Rollers &amp; Compaction Equipment</li><li>Track Loaders / Posi Tracks</li></ul>
  <ul class="list" style="left:149px;top:353px;line-height:12.4px"><li>Tipper Trucks &amp; Quad Dogs</li><li>Water Carts</li><li>Tilt Hitches &amp; Attachments</li></ul>
  <ul class="list" style="left:249px;top:353px;line-height:12.4px"><li>Dozers</li><li style="margin-left:-6px">Tool &amp; Service Trucks</li></ul>
  <div class="foot"><span class="no">02</span>|<span>ARDENT CIVIL GROUP</span><span>| CAPABILITY STATEMENTS</span><span class="bar"></span></div>
</section>

<!-- Stormwater -->
<section class="page p3">
  <div class="photo" role="img" aria-label="Concrete stormwater pit risers stacked on site" style="left:158px;top:0;width:184px;height:198px;background:linear-gradient(120deg,#2a221c,#5b5650 45%,#c9c8c4 60%,#8e8b86 80%,#3a2f25)"></div>
  <div class="brand"><span class="name">ARDENT</span><span class="sub">CIVIL GROUP</span></div>
  <div class="tags">EARTHWORKS<span>|</span>INFRASTRUCTURE<span>|</span>PLANT HIRE</div>
  <div class="title" style="top:99px;font-size:26px">STORMWATER &amp;<br><span class="teal" style="font-size:21px">CIVIL INFRASTRUCTURE</span></div>
  <div class="rule" style="top:150px"></div>
  <div class="lede" style="top:157px">Delivering complex drainage, utility and civil<br>infrastructure solutions.<br><em>across NSW</em></div>
  <div class="divider" style="top:198px"></div>
  <div class="card" style="left:21px;top:212px;width:98px;height:79px"><div class="photo" role="img" aria-label="Deep drainage trench with shoring box" style="inset:0;background:linear-gradient(180deg,#6b7b86,#7b4a2e 45%,#5b3a26)"></div><div class="tile-label">DEEP DRAINAGE INSTALLATION</div></div>
  <div class="card" style="left:123px;top:212px;width:98px;height:79px"><div class="photo" role="img" aria-label="Lined retention basin under blue sky" style="inset:0;background:linear-gradient(180deg,#3d7fd6,#8fb3d8 40%,#cfd8df 60%,#8a6a48)"></div><div class="tile-label">RETENTION BASINS</div></div>
  <div class="card" style="left:21px;top:294px;width:98px;height:79px"><div class="photo" role="img" aria-label="Utility and service trench with conduits" style="inset:0;background:linear-gradient(180deg,#9aa2a6,#6f5a48 45%,#3f3128)"></div><div class="tile-label">UTILITY &amp; SERVICE TRENCHES</div></div>
  <div class="card" style="left:123px;top:294px;width:98px;height:79px"><div class="photo" role="img" aria-label="Headwall and outlet pipe with rock protection" style="inset:0;background:linear-gradient(180deg,#4a7fc4,#5a4330 40%,#b7a99a 75%,#6e665e)"></div><div class="tile-label">HEADWALLS &amp; OUTLET STRUCTURES</div></div>
  <div class="h" style="left:234px;top:212px">Core Services</div>
  <ul class="list" style="left:234px;top:229px;line-height:14.5px"><li>Stormwater Drainage</li><li>RRJ Pipe Installation</li><li>GPT Installation</li><li>Junction Pits &amp; Manholes</li><li>Utility Relocations</li><li>Retention Basins</li><li>Headwalls &amp; Culverts</li><li>Deep Excavation</li><li>Civil Infrastructure</li><li>GPS Controlled Excavation</li></ul>
  <div class="h" style="left:21px;top:384px">Core Services</div>
  <div class="abs" style="left:105px;top:386px;font-size:5.8px;color:var(--grey);line-height:1.6">Stormwater &nbsp;| &nbsp;Utilities &nbsp;| &nbsp;Drainage &nbsp;| &nbsp;Gpts &nbsp;| &nbsp;Retention basins &nbsp;| &nbsp;Civil<br>infrastructure</div>
  <div class="divider" style="top:407px"></div>
  <div class="foot"><span class="no">03</span>|<span>ARDENT CIVIL GROUP</span><span>| CAPABILITY STATEMENTS</span><span class="bar"></span></div>
</section>

<!-- Bulk earthworks -->
<section class="page p4">
  <div class="photo" role="img" aria-label="Excavator loading a dump truck across a large earthworks site" style="left:157px;top:0;width:185px;height:212px;background:linear-gradient(150deg,#5e7f4a,#8a7a5e 30%,#b09470 55%,#5f4c38 85%,#2a2520)"></div>
  <div class="brand"><span class="name">ARDENT</span><span class="sub">CIVIL GROUP</span></div>
  <div class="tags">EARTHWORKS<span>|</span>INFRASTRUCTURE<span>|</span>PLANT HIRE</div>
  <div class="title" style="top:99px;font-size:20.5px">BULK EARTHWORKS &amp;<br><span class="teal" style="font-size:26px;line-height:1">SUBDIVISION<br>DEVELOPMENT</span></div>
  <div class="rule" style="top:176px"></div>
  <div class="lede" style="top:182px">Delivering large-scale earthworks, road<br>formation, cut-to-fill operations &amp; subdivision<br>infrastructure projects <em>across NSW.</em></div>
  <div class="divider" style="top:212px"></div>
  <div class="card" style="left:21px;top:220px;width:94px;height:164px">
    <div class="photo" role="img" aria-label="Stepped cut batters on a cleared site" style="left:0;top:0;right:0;height:98px;background:linear-gradient(180deg,#4d82c8,#7a8c6a 35%,#a3583a 60%,#7a6048)"></div>
    <div class="cap" style="top:107px;font-size:5.6px"><b>DETAILED EXCAVATION &amp;<br>CUT-TO-FILL OPERATIONS</b><span style="display:block;margin-top:3px">Precise excavation, bulk cut and fill operations with GPS accuracy.</span></div>
  </div>
  <div class="card" style="left:120px;top:220px;width:91px;height:83px">
    <div class="photo" role="img" aria-label="Water cart truck spraying a haul road" style="left:0;top:0;right:0;height:42px;background:linear-gradient(180deg,#4d86d4,#dfe3e6 55%,#6b6a5f)"></div>
    <div class="cap" style="top:46px"><b>DUST SUPPRESSION &amp;<br>COMPACTION SUPPORT</b>Water cart services to maintain safety, quality and compliance</div>
  </div>
  <div class="card" style="left:120px;top:306px;width:91px;height:78px">
    <div class="photo" role="img" aria-label="Aerial view of subdivision earthworks with machinery" style="left:0;top:0;right:0;height:38px;background:linear-gradient(160deg,#6b6450,#a88c66 50%,#7a6a4e)"></div>
    <div class="cap" style="top:42px"><b>SUBDIVISION<br>INFRASTRUCTURE DELIVERY</b>Full-service delivery of subdivision earthworks and infrastructure</div>
  </div>
  <div class="h" style="left:221px;top:225px;line-height:1.1;font-size:9.5px">Earthworks<br>Capabilities</div>
  <ul class="list" style="left:221px;top:249px;line-height:12.3px"><li>Bulk Earthworks</li><li>GPS Machine Control</li><li>Cut &amp; Fill Operations</li><li>Detailed Excavation</li><li>Rock Excavation</li><li>Road Formation</li><li>Final Trim</li><li>Retention Basins</li><li>Subdivision Development</li><li>Water Cart Services</li><li>Plant Hire</li></ul>
  <div class="h" style="left:21px;top:391px">Project Delivery</div>
  <div class="abs" style="left:123px;top:392px;font-size:5.8px;color:var(--grey);line-height:1.6">Bulk Earthworks &nbsp;| &nbsp;Cut &amp; Fill operations &nbsp;| &nbsp;Gps Control &nbsp;| &nbsp;Final Trim<br>Subdivisions | Roadworks</div>
  <div class="divider" style="top:413px"></div>
  <div class="foot"><span class="no">04</span>|<span>ARDENT CIVIL GROUP</span><span>| CAPABILITY STATEMENTS</span><span class="bar"></span></div>
</section>

<!-- Fleet -->
<section class="page p5">
  <div class="photo" role="img" aria-label="Teal excavator working on a large earthworks site with trucks behind" style="left:152px;top:0;width:190px;height:198px;background:linear-gradient(150deg,#2e5a2a,#7a7a58 25%,#b69a74 50%,#8c7152 80%,#4a3a2a)"></div>
  <div class="brand"><span class="name">ARDENT</span><span class="sub">CIVIL GROUP</span></div>
  <div class="tags">EARTHWORKS<span>|</span>INFRASTRUCTURE<span>|</span>PLANT HIRE</div>
  <div class="title" style="top:99px;font-size:20.5px">OUR<br><span class="teal" style="font-size:27px;line-height:1.05">FLEET &amp; PLANT</span></div>
  <div class="rule" style="top:155px"></div>
  <div class="lede" style="top:159px">Modern, GPS-equipped plant and support<br>equipment delivering safe, productive and<br>reliable outcomes across civil infrastructure<br>projects throughout <em>NSW</em></div>
  <div class="divider" style="top:198px"></div>
  <div class="card" style="left:21px;top:211px;width:93px;height:167px">
    <div class="photo" role="img" aria-label="Large concrete pipe being laid in a shored trench" style="left:0;top:0;right:0;height:99px;background:linear-gradient(180deg,#6b5a44,#a08a6c 40%,#c8c6c0 60%,#5e4a38)"></div>
    <div class="cap" style="top:103px;font-size:5.8px;line-height:1.5"><b>SPECIALISED EQUIPMENT</b>Purpose-built attachments and support equipment to complete complex civil infrastructure works safely and efficiently.</div>
  </div>
  <div class="h" style="left:126px;top:216px">Fleet Capability</div>
  <ul class="list" style="left:126px;top:232px;line-height:12.3px"><li>Excavators 1.7T-50T</li><li>GPS Machine Control</li><li>Tilt Hitch Equipped</li><li>Rock Breakers</li><li>Augers &amp; Compaction Wheels</li><li>Detailed Excavation</li><li>Bulk Earthworks</li><li>Final Trim Operations</li><li>Water Carts</li><li>Transport &amp; Site Support</li><li>Attachments for all applications</li><li>Fully Maintained &amp; Serviced</li></ul>
  <div class="card" style="left:229px;top:211px;width:91px;height:82px">
    <div class="photo" role="img" aria-label="Water cart truck on site" style="left:0;top:0;right:0;height:41px;background:linear-gradient(180deg,#4d86d4,#e2e5e8 55%,#6b6a5f)"></div>
    <div class="cap" style="top:45px"><b>WATER CART SERVICES</b>Dust suppression &amp; compaction support to maintain safety, quality &amp; compliance on every project.</div>
  </div>
  <div class="card" style="left:229px;top:296px;width:91px;height:82px">
    <div class="photo" role="img" aria-label="Aerial view of plant working across an earthworks site" style="left:0;top:0;right:0;height:41px;background:linear-gradient(160deg,#6b6450,#a88c66 50%,#7a6a4e)"></div>
    <div class="cap" style="top:45px"><b>MODERN, RELIABLE &amp; READY</b>A modern fleet that is well maintained, fully serviced &amp; ready to perform from day one.</div>
  </div>
  <div class="mini-stats">
    <div><i></i><span><b>13+ Pieces of Plant</b>Excavators, loaders, rollers,<br>dump trucks and more.</span></div>
    <div><i></i><span><b>6+ Service vehicles</b>Utes, tool trucks &amp; support<br>vehicles</span></div>
    <div><i></i><span><b>GPS Machine Control</b>Survey GPS systems for<br>precision &amp; productivity</span></div>
    <div><i></i><span><b>ISO accredited systems</b>Quality safety &amp; environmental<br>management systems.</span></div>
  </div>
  <div class="foot"><span class="no">05</span>|<span>ARDENT CIVIL GROUP</span><span>| CAPABILITY STATEMENTS</span><span class="bar"></span></div>
</section>

<!-- Brand mark -->
<div class="mark">
  <span class="name">ARDENT</span>
  <span class="sub">CIVIL GROUP</span>
  <div class="ln"></div>
  <div class="tg"><span>EARTHWORKS</span><span style="color:var(--aqua)">|</span><span>INFRASTRUCTURE</span><span style="color:var(--aqua)">|</span><span>PLANT HIRE</span></div>
</div>

</body>
</html>
```